Building company buisness cards

We are looking for a sharp modern new look for our business cards.
We are a New Zealand based company that specialises in house and land packages.
We have attached a photo of the current logo and would like to see if it can be improved somehow if needed.
We are open to any colours but we have chosen green at this stage.
Feel free to change the font and make the logo smarter looking.
Play with the colours and see what looks best.

We want a card that looks so good know one will want to throw it away!

Target Market(s)

Home buyers

Industry/Entity Type

Building

Contact Information for Business Card

Garth Ellery
0219364028
gellery@tidewaterhomecraft.co.nz
tidewaterhomecraft.co.nz

Font styles to use
Serif
Sans Serif

Colors

Designer to choose colors to be used in the design.

Requirements
Must have
• Logo and company name on one side, details on the other side
Nice to have
• Color codes for the original green are HEX #4a8028, RGB(74,128,40), CMYK(42,0,69,50)
• Round corners, Raised and/or spot UV

```html
<!DOCTYPE html>
<html lang="en">
<head>
<meta charset="utf-8">
<title>Tidewater Homecraft – Business Cards</title>
<link href="https://fonts.googleapis.com/css2?family=Lato:wght@400&family=Nunito:wght@800&display=swap" rel="stylesheet">
<style>
  :root {
    --backdrop: #5b5b5b;
    --brand-green: #4a8028;
    --figure-tint: #7fa865;
    --ink: #ffffff;
    --rule: rgba(255,255,255,0.35);
  }
  * { margin: 0; padding: 0; box-sizing: border-box; }
  html, body { width: 1200px; height: 802px; overflow: hidden; }
  body { background: var(--backdrop); position: relative; font-family: "Lato", Arial, sans-serif; color: var(--ink); }

  .card {
    position: absolute; top: 274px; width: 443px; height: 264px;
    background: var(--brand-green); overflow: hidden;
    box-shadow: 2px 3px 6px rgba(0,0,0,0.45);
  }
  .card--details { left: 136px; }
  .card--brand { left: 624px; }

  .family-artwork {
    position: absolute; left: 0; top: 0; width: 214px; height: 264px;
    background: linear-gradient(180deg, var(--figure-tint), var(--brand-green));
  }

  .wordmark { font-family: "Nunito", Arial, sans-serif; font-weight: 800; letter-spacing: 0.2px; line-height: 1; }

  .details-block { position: absolute; right: 20px; top: 0; text-align: right; }
  .details-block .wordmark-line { position: absolute; right: 0; white-space: nowrap; }
  .details-block .wordmark-top { top: 67px; font-size: 18px; }
  .details-block .wordmark-bottom { top: 88px; font-size: 22px; }
  .details-block .rule { position: absolute; right: 90px; top: 116px; width: 40px; height: 1px; background: var(--rule); }
  .holder-name { position: absolute; right: 0; top: 148px; font-size: 16px; white-space: nowrap; letter-spacing: 0.2px; }
  .contact-list { position: absolute; right: 0; top: 190px; list-style: none; font-size: 11.5px; white-space: nowrap; }
  .contact-list li { height: 16px; display: flex; justify-content: flex-end; align-items: center; gap: 4px; }
  .contact-list svg { width: 10px; height: 10px; fill: var(--ink); }

  .brand-block { position: absolute; inset: 0; text-align: center; }
  .brand-block .wordmark-top { position: absolute; left: 0; right: 0; top: 129px; font-size: 26px; }
  .brand-block .wordmark-bottom { position: absolute; left: 0; right: 0; top: 159px; font-size: 34px; }
  .brand-block .rule { position: absolute; left: 200px; top: 200px; width: 62px; height: 1px; background: var(--rule); }
</style>
</head>
<body>
  <section class="card card--details">
    <div class="family-artwork" role="img" aria-label="Illustration of a parent holding hands with a child"></div>
    <div class="details-block">
      <div class="wordmark wordmark-line wordmark-top">tidewater</div>
      <div class="wordmark wordmark-line wordmark-bottom">homecraft.</div>
      <div class="rule"></div>
      <p class="holder-name">GARTH ELLERY</p>
      <ul class="contact-list">
        <li>0219364028
          <svg viewBox="0 0 10 10" aria-hidden="true"><path d="M1 4 C1 2 9 2 9 4 L7.5 4.5 L7 3.5 L3 3.5 L2.5 4.5 Z M2.5 5 L7.5 5 L8.5 9 L1.5 9 Z"/></svg>
        </li>
        <li>gellery@tidewaterhomecraft.co.nz
          <svg viewBox="0 0 10 10" aria-hidden="true"><path d="M0.5 2 H9.5 V8 H0.5 Z M1 2.5 L5 5.5 L9 2.5" stroke="#4a8028" stroke-width="0.8"/></svg>
        </li>
        <li>www.tidewaterhomecraft.co.nz
          <svg viewBox="0 0 10 10" aria-hidden="true"><circle cx="5" cy="5" r="4.5"/><path d="M3 3 L5 2.5 L5.5 4.5 L4 6 L3 5 Z M6 6 L7.5 5.5 L7 8 Z" fill="#4a8028"/></svg>
        </li>
      </ul>
    </div>
  </section>

  <section class="card card--brand">
    <div class="brand-block">
      <div class="wordmark wordmark-top">tidewater</div>
      <div class="wordmark wordmark-bottom">homecraft.</div>
      <div class="rule"></div>
    </div>
  </section>
</body>
</html>
```